Veloran Pumps needs a creative posters design

To design 5 pieces of posters - (1 set of 2 posters and 1 set of 3 posters) Design must be professional, creative, eye catchy and clean, exclusive feel.
Use of corporate yellow color but mix well with black and/ or white to make the yellow stand out.
Corporate yellow - Pantone 3955C
These posters are used in the product showroom of the white wall.
Product photos can be cropped.
You can add some background if you need to.

Target Market(s)

Professional, b to be

Industry/Entity Type

It Professional

Font styles to use
Serif
Sans Serif

Requirements
Must have
• creative, eye catchy, use of corporate yellow color with either/ both black and/ or white, clean look
Nice to have
• Creativity, Professionalism, Clean and Exclusive Look
Should not have
• Crowded and complicated

```html
<!DOCTYPE html>
<html lang="en">
<head>
<meta charset="utf-8">
<title>Veloran Pumps – Showroom Posters</title>
<link href="https://fonts.googleapis.com/css2?family=EB+Garamond:wght@400&family=Roboto:wght@300;400;900&family=Roboto+Condensed:ital,wght@0,700;1,700&display=swap" rel="stylesheet">
<style>
  :root{
    --yellow:#f3e000;
    --black:#231f20;
    --white:#ffffff;
    --navy:#201d6e;
    --stage:#84a152;
    --ring:#dcdce4;
    --grey-text:#4a4a4a;
  }
  *{box-sizing:border-box;margin:0;padding:0}
  html,body{width:1200px;height:1112px;overflow:hidden;background:var(--stage)}
  .canvas{position:relative;width:1200px;height:1112px}
  .poster{position:absolute;width:362px;height:511px;overflow:hidden}

  /* brand mark */
  .brand-circle{position:absolute;border:6px solid var(--navy);border-radius:50%}
  .brand-name{position:absolute;text-align:center;font-family:"Roboto Condensed",sans-serif;font-weight:700;color:var(--navy);letter-spacing:0;line-height:1}

  /* vision / mission */
  .statement{position:absolute;right:20px;text-align:right;font-family:"EB Garamond",serif;font-size:12px;line-height:15px}
  .statement-title{position:absolute;right:0;font-family:"EB Garamond",serif;font-weight:400;font-size:19px;padding:0 20px 2px 0;border-bottom:1.5px solid var(--black)}
  .vision{background:var(--white)}
  .mission{background:var(--yellow)}

  /* product posters */
  .product{background:linear-gradient(180deg,var(--yellow) 0%,var(--yellow) 38%,#f8ee70 62%,var(--white) 86%)}
  .tagline{position:absolute;left:0;width:100%;text-align:center;font-family:"Roboto",sans-serif;font-weight:300;font-size:10px;letter-spacing:.6px;color:var(--grey-text)}
  .tagline b{font-weight:900;color:var(--black)}
  .product-shot{position:absolute;border-radius:8px;background:linear-gradient(90deg,#8d8f92 0%,#e9eaeb 35%,#bfc1c3 60%,#7d7f82 100%)}
  .bubble{position:absolute;border-radius:50%;display:flex;align-items:center;justify-content:center;text-align:center;padding:9px;font-family:"Roboto Condensed",sans-serif;font-style:italic;font-weight:700;font-size:9px;line-height:11px}
  .bubble.light{background:var(--white);color:var(--black);border:3px solid var(--black)}
  .bubble.dark{background:var(--black);color:var(--white);border:3px solid var(--white);box-shadow:0 0 0 1.5px var(--black)}
  .bubble.dark.accent{color:var(--yellow)}
  .bubble .plain{font-family:"Roboto",sans-serif;font-style:normal;font-weight:300;font-size:11px;line-height:12px}
  .series{position:absolute;background:var(--black);color:var(--white);border-radius:14px;display:flex;flex-direction:column;align-items:center;justify-content:center;font-family:"Roboto",sans-serif;font-weight:300;font-size:19px;line-height:21px;letter-spacing:-.3px;white-space:nowrap}
  .series b{font-weight:900;color:var(--yellow)}
</style>
</head>
<body>
<main class="canvas">

  <!-- Vision -->
  <section class="poster vision" style="left:29px;top:32px">
    <svg width="362" height="511" style="position:absolute;left:0;top:0" aria-hidden="true">
      <defs><clipPath id="vision-disc"><circle cx="330" cy="538" r="298"/></clipPath></defs>
      <circle cx="238" cy="390" r="200" fill="none" stroke="var(--ring)" stroke-width="22"/>
      <circle cx="330" cy="538" r="298" fill="var(--yellow)"/>
      <rect x="0" y="373" width="362" height="140" fill="var(--black)" clip-path="url(#vision-disc)"/>
    </svg>
    <div class="brand-circle" style="left:52px;top:18px;width:94px;height:94px"></div>
    <div class="brand-name" style="top:124px;left:19px;width:160px;font-size:44px">VELORAN</div>
    <h2 class="statement-title" style="top:290px;color:var(--black)">Vision</h2>
    <p class="statement" style="top:324px;color:var(--black)">To be the recognized leader in the<br>deep well pumps markets, as measured<br>by quality, service and growth.</p>
    <p class="statement" style="top:387px;color:var(--white)">Our vision is a challenge and it takes a<br>lot of determination, commitment and most<br>importantly, passion to succeed.</p>
    <p class="statement" style="top:437px;color:var(--yellow)">Our passion for excellence is a formidable<br>force that will carry us relentlessly to meet and<br>exceed our challenge, we believe in it,<br>we fight for it and we will deliver.</p>
  </section>

  <!-- Mission -->
  <section class="poster mission" style="left:416px;top:32px">
    <svg width="362" height="511" style="position:absolute;left:0;top:0" aria-hidden="true">
      <polygon points="362,0 362,511 0,511" fill="var(--black)"/>
    </svg>
    <div class="brand-circle" style="left:53px;top:18px;width:94px;height:94px"></div>
    <div class="brand-name" style="top:124px;left:20px;width:160px;font-size:44px">VELORAN</div>
    <h2 class="statement-title" style="top:298px;color:var(--yellow);border-color:var(--yellow)">Mission</h2>
    <p class="statement" style="top:332px;color:var(--white)">We are committed to providing<br>our customers with the products that have<br>differentiated and value added features.</p>
    <p class="statement" style="top:387px;color:var(--yellow)">We knew from the beginning that<br>breaking into the market already dominated<br>by established brands will be a challenge.</p>
    <p class="statement" style="top:440px;color:var(--yellow)">Doing exactly what they are doing will not<br>be an option.  Innovation through product<br>differentiation is the only solution.</p>
  </section>

  <!-- 4" oil filled motor -->
  <section class="poster product" style="left:803px;top:288px">
    <div class="brand-circle" style="left:146px;top:18px;width:70px;height:70px"></div>
    <div class="brand-name" style="top:92px;left:0;width:100%;font-size:34px">VELORAN</div>
    <p class="tagline" style="top:160px">MADE WITH <b>PRIDE</b></p>
    <div class="product-shot" role="img" aria-label="Photo of the stainless steel 4 inch oil filled submersible motor" style="left:147px;top:178px;width:73px;height:268px"></div>
    <div class="bubble light" style="left:61px;top:206px;width:90px;height:90px">Manufactured according to the International Standard</div>
    <div class="bubble dark accent" style="left:59px;top:286px;width:92px;height:92px">Fitted with Italian mechanical seal and oversized bearing</div>
    <div class="bubble dark" style="left:207px;top:217px;width:90px;height:90px">CLASS F INSULATION AND IP 68 PROTECTION</div>
    <div class="bubble light" style="left:202px;top:291px;width:100px;height:100px">Motor Top Bracket available in both Brass and Stainless Steel over Cast Iron</div>
    <div class="series" style="left:33px;top:452px;width:295px;height:47px"><span>“4” VM OIL <b>FILLED MOTOR</b></span><span>SERIES</span></div>
  </section>

  <!-- 4" pump -->
  <section class="poster product" style="left:29px;top:567px">
    <div class="brand-circle" style="left:145px;top:16px;width:70px;height:70px"></div>
    <div class="brand-name" style="top:92px;left:0;width:100%;font-size:34px">VELORAN</div>
    <p class="tagline" style="top:170px">MADE WITH <b>PRIDE</b></p>
    <div class="product-shot" role="img" aria-label="Photo of the 4 inch stainless steel submersible pump" style="left:152px;top:187px;width:58px;height:248px"></div>
    <div class="bubble light" style="left:68px;top:258px;width:90px;height:90px">The Floating Impeller Stack and Face Clearance Design for optimum resistance against sand</div>
    <div class="bubble dark" style="left:207px;top:227px;width:76px;height:76px">Maximum permissible quantity of sand 150 g/m3</div>
    <div class="bubble dark accent" style="left:206px;top:303px;width:78px;height:78px">Made of Japanese raw materials for impellers and diffusers</div>
    <div class="series" style="left:68px;top:443px;width:224px;height:27px"><span>“4” <b>VX PUMP</b> SERIES</span></div>
  </section>

  <!-- 6" & 8" pump -->
  <section class="poster product" style="left:416px;top:567px">
    <div class="brand-circle" style="left:146px;top:16px;width:70px;height:70px"></div>
    <div class="brand-name" style="top:92px;left:0;width:100%;font-size:34px">VELORAN</div>
    <p class="tagline" style="top:159px">MADE WITH <b>PRIDE</b></p>
    <div class="product-shot" role="img" aria-label="Photo of the cast stainless steel pump shown in cutaway with its impeller stages" style="left:160px;top:175px;width:48px;height:272px;background:linear-gradient(90deg,#5f6164 0%,#d9dadb 25%,#2b2b2b 50%,#c9cacc 75%,#6a6c6f 100%)"></div>
    <div class="bubble light" style="left:71px;top:208px;width:88px;height:88px">The Full Casted Stainless Steel pump for the utmost durability in the sandy water</div>
    <div class="bubble dark accent" style="left:66px;top:290px;width:94px;height:94px">Compared to the Stamped Fabricated Stainless Steel parts, the Casted parts are more solid, thicker and tougher.</div>
    <div class="bubble dark" style="left:209px;top:210px;width:84px;height:84px"><span>NO welding point<br><span class="plain">NO point of weaknesses</span></span></div>
    <div class="bubble light" style="left:207px;top:292px;width:92px;height:92px">By Lost Wax Investment Casting Process for smoother surfaces and solid structure</div>
    <div class="series" style="left:47px;top:451px;width:268px;height:27px"><span>“6” &amp; 8” <b>KRV PUMP</b> SERIES</span></div>
  </section>

</main>
</body>
</html>
```